quillcrestPRESS is launching 2 new eBooks and needs beautiful and compelling cover designs and a desig

We are launching 2 non-fiction eBooks that are part of a series but will be launched separately, so we would like to see some continuity between the 2 designs - but each should have a strong stand alone identity.

The eBooks are both in the naturopathic/holistic health niche.

ebook 1 title is:
Shaping Your Perfect Studio
(sub) The Wellness Manual to growing your own thriving natural and
alternative therapy business.

The book is a comprehensive guide for naturopaths and other alternative health providers - ( Naturopath,
Nutritionist, Homeopath, Acupuncturist, Chiropractor,
Massage Therapist, or Holistic Health Specialist), who are seeking to setup their own, profitable naturopathic business.

ebook 2 title is:
Silver Handshakes (subtitle) Win 40 + Patients Inside Six Weeks

(sub/sub)27 methods to promote your natural and alternative therapy business

This book is a list of 32 tips for the same audience to increase there customer referrals (and therefore income).

Each book should feature
written by Moira Tennant
published by Tennant Publishing

Each book should feature the authors photograph on the cover (attached) - no caveats on cropping etc - whatever fits with the design.

You can see more about the writer on her website here:

http://www.harbourleafwellness.example.au/

What we require:

1) cover art for both eBooks that conforms to Kindle and iPad specs
2) Flat & 3D book cover art for use on website and marketing campaigns
3) we will require layered PSD files on completion of project.

I'd like to add that we are seeking to build a relationship with the designer we choose for this project, as we are publishing many other titles throughout 2014

Many eBook writers jump straight to Gigly for a cover. The result is most self published books have the same generic look the 'gigly' look.

I don't want that look.

We want to reward great design and ensure quillcrestPRESS eBook titles have a great look.

The winning designer will be working with us on many more projects.

Colin Marsh
quillcrestPRESS

```html
<!DOCTYPE html>
<html lang="en">
<head>
<meta charset="utf-8">
<title>Shaping Your Perfect Studio – Book Cover Spread</title>
<link rel="stylesheet" href="https://fonts.googleapis.com/css2?family=Oswald:wght@400;500;700&family=Parisienne&display=swap">
<style>
  :root {
    --teal: #31cdd0;
    --teal-light: #8fdfe0;
    --teal-dark: #127474;
    --teal-strip: #3fc3c6;
    --paper: #dedede;
    --paper-light: #e8e8e8;
    --green: #b6e69c;
    --mint: #b9f0c4;
    --shadow: #5b5b5b;
    --yellow: #fff200;
    --mauve: #8a5d6c;
    --script: #7a6a78;
    --cyan-label: #38d6d9;
    --white: #ffffff;
    --title-font: "Oswald", sans-serif;
    --body-font: "Oswald", sans-serif;
    --script-font: "Parisienne", cursive;
  }
  * { margin: 0; padding: 0; box-sizing: border-box; }
  html, body { width: 1200px; height: 850px; overflow: hidden; background: var(--teal); }
  .spread { position: relative; width: 1200px; height: 850px; overflow: hidden; }
  .abs { position: absolute; }
  .shapes { position: absolute; inset: 0; }

  .title-3d {
    font-family: var(--title-font);
    font-weight: 700;
    color: var(--green);
    text-transform: uppercase;
    line-height: 1;
    white-space: nowrap;
    text-shadow: -1px 1px 0 var(--shadow), -2px 2px 0 var(--shadow), -3px 3px 0 var(--shadow),
                 -4px 4px 0 var(--shadow), -5px 5px 0 var(--shadow), -6px 6px 0 var(--shadow),
                 -7px 7px 0 var(--shadow), -8px 8px 0 var(--shadow);
  }
  .title-3d.small {
    text-shadow: -1px 1px 0 var(--shadow), -2px 2px 0 var(--shadow), -3px 3px 0 var(--shadow);
  }
  .title-3d.circle-word { color: var(--yellow); }

  /* back cover */
  .back-title { left: 95px; width: 230px; text-align: center; font-size: 46px; }
  .back-title.line-1 { top: 14px; }
  .back-title.line-2 { top: 142px; }
  .back-circle-words {
    left: 170px; top: 82px; width: 80px; text-align: center; font-size: 21px; line-height: 1.05;
  }
  .back-subtitle {
    left: 10px; top: 222px; width: 410px; text-align: center;
    font-family: var(--script-font); font-size: 31px; line-height: 1.2; color: var(--script);
  }
  .back-rule { left: 62px; top: 376px; width: 308px; height: 3px; background: #6d7f80; }
  .author-photo {
    background: linear-gradient(160deg, #e9e4df 0%, #d6c4b4 45%, #8a4a5a 75%, #3b3236 100%);
  }
  .back-photo { left: 20px; top: 404px; width: 118px; height: 177px; }
  .author-bio {
    left: 20px; top: 404px; width: 370px;
    font-family: var(--body-font); font-size: 14.5px; line-height: 1.62;
    text-transform: uppercase; color: var(--mauve); text-align: left;
  }
  .author-bio .wrap-space { float: left; width: 128px; height: 184px; }

  .credit { font-family: var(--body-font); text-transform: uppercase; text-align: right; line-height: 1; }
  .credit .label { color: var(--cyan-label); font-weight: 500; font-size: 20px; }
  .credit .name { font-family: var(--title-font); font-weight: 700; font-size: 28px; }
  .back-credit { left: 20px; top: 686px; width: 305px; }
  .back-credit .label, .back-credit .name { display: block; margin-bottom: 5px; }

  /* spine */
  .spine-title {
    left: 624px; top: 40px; font-size: 48px;
    transform-origin: 0 0; transform: rotate(90deg);
  }
  .spine-credit {
    left: 614px; top: 686px; transform-origin: 0 0; transform: rotate(90deg);
    font-family: var(--body-font); text-transform: uppercase; line-height: 1; white-space: nowrap;
  }
  .spine-credit span { display: block; }
  .spine-credit .label { color: var(--cyan-label); font-size: 9px; }
  .spine-credit .name { color: var(--shadow); font-size: 13px; font-weight: 700; }

  /* front cover */
  .front-line-1, .front-line-2 { font-size: 118px; transform: rotate(-13deg); transform-origin: left top; }
  .front-line-1 { left: 696px; top: 96px; }
  .front-line-2 { left: 786px; top: 448px; }
  .front-circle-words {
    left: 815px; top: 238px; width: 180px; text-align: center; font-size: 54px; line-height: 1;
    transform: rotate(-13deg);
    text-shadow: -1px 1px 0 var(--shadow), -2px 2px 0 var(--shadow), -3px 3px 0 var(--shadow),
                 -4px 4px 0 var(--shadow), -5px 5px 0 var(--shadow);
  }
  .front-subtitle {
    left: 640px; top: 575px; width: 560px; text-align: center;
    font-family: var(--script-font); font-size: 33px; line-height: 1.25; color: var(--mint);
    transform: rotate(-16deg);
  }
  .front-credit { left: 830px; top: 728px; width: 240px; }
  .front-credit .label { color: var(--shadow); font-size: 18px; }
  .front-credit .name { font-size: 27px; color: var(--shadow); }
  .front-credit span { display: block; margin-bottom: 3px; }
  .front-photo { left: 1088px; top: 720px; width: 80px; height: 118px; }
</style>
</head>
<body>
<main class="spread">
  <svg class="shapes" width="1200" height="850" viewBox="0 0 1200 850" aria-hidden="true">
    <rect x="0" y="0" width="430" height="850" fill="var(--teal)"/>
    <rect x="430" y="0" width="110" height="850" fill="var(--paper-light)"/>
    <rect x="540" y="0" width="92" height="850" fill="var(--paper)"/>
    <rect x="632" y="0" width="284" height="850" fill="var(--teal)"/>
    <rect x="916" y="0" width="284" height="850" fill="var(--teal-light)"/>
    <line x1="568" y1="18" x2="1200" y2="18" stroke="var(--white)" stroke-width="4"/>
    <line x1="568" y1="16" x2="568" y2="650" stroke="var(--white)" stroke-width="4"/>
    <rect x="0" y="660" width="632" height="160" fill="var(--teal-dark)"/>
    <rect x="0" y="820" width="632" height="15" fill="var(--teal-strip)"/>
    <rect x="0" y="835" width="632" height="15" fill="var(--teal-dark)"/>
    <polygon points="632,660 1200,488 1200,650 632,820" fill="var(--teal-dark)"/>
    <polygon points="632,820 1200,650 1200,664 632,835" fill="var(--teal-strip)"/>
    <circle cx="210" cy="105" r="38" fill="var(--yellow)"/>
    <circle cx="905" cy="305" r="110" fill="var(--yellow)"/>
    <rect x="333" y="683" width="2" height="115" fill="#7aa"/>
    <rect x="1077" y="722" width="2" height="116" fill="var(--shadow)"/>
  </svg>

  <!-- back cover -->
  <h2 class="abs title-3d small back-title line-1">Shaping</h2>
  <p class="abs title-3d small back-circle-words">Your<br>Perfect</p>
  <p class="abs title-3d small back-title line-2">Studio</p>
  <p class="abs back-subtitle">The Wellness Manual to<br>growing your own thriving<br>Natural and Alternative<br>Therapy Business.</p>
  <div class="abs back-rule"></div>
  <div class="abs author-photo back-photo" role="img" aria-label="Portrait photograph of author Moira Tennant"></div>
  <p class="abs author-bio"><span class="wrap-space"></span>&nbsp;&nbsp;&nbsp;Moira Tennant is a naturopath and graduate of the Coastal College of Natural Medicine, Queensland, with a bachelor degree of health science (naturopathy), advanced diploma of health science (naturopathy), diploma of herbal medicine, diploma of nutrition, certificate I biomesotherapy/biopuncture, diploma of bioresonance therapy.</p>
  <div class="abs credit back-credit">
    <span class="label">Written by</span>
    <span class="name title-3d small">Moira Tennant</span>
    <span class="label">Published by</span>
    <span class="name title-3d small">Tennant Publishing</span>
  </div>

  <!-- spine -->
  <h2 class="abs title-3d small spine-title">Shaping Your Perfect Studio</h2>
  <div class="abs spine-credit">
    <span class="label">Written by</span>
    <span class="name">Moira Tennant</span>
    <span class="label">Published by</span>
    <span class="name">Tennant Publishing</span>
  </div>

  <!-- front cover -->
  <h1 class="abs title-3d front-line-1">Shaping</h1>
  <p class="abs title-3d circle-word front-circle-words">Your<br>Perfect</p>
  <p class="abs title-3d front-line-2">Studio</p>
  <p class="abs front-subtitle">The Wellness Manual to<br>growing your own thriving Natural<br>and Alternative Therapy Business</p>
  <div class="abs credit front-credit">
    <span class="label">Written by</span>
    <span class="name">Moira Tennant</span>
    <span class="label">Published by</span>
    <span class="name">Tennant Publishing</span>
  </div>
  <div class="abs author-photo front-photo" role="img" aria-label="Portrait photograph of author Moira Tennant"></div>
</main>
</body>
</html>
```